Lead Generating Website Design

We are looking for a brand new design for our existing website.
The existing website is www.brivopartners.com
The website is aimed at businesses that would like to licence the courses from our school to sell themselves.
We want the menu to be the following:
* Home
* About us
* Our Courses
* LMS Platform
* Affiliate Program
* Contact Us
We want the colour scheme to use the following design guide:
https://folioshelf.net/stepsforward/docs/glide_and_wander_brand_guidelines
Like the idea of the circles and colours in the style guide for places. Want lots of white areas as well as coloured areas
An example of a nice looking site is : https://www.studyharbor.online/
MUST look good on mobile also
On the home page we want the following:
A large image with the text :
Over 450 courses written by highly qualified academics with real world experience.
The 'Join our thriving group of Affiliates - start your own online college!' section on the current website with the text and becoming an affiliate video
A section for 'see how our LMS works' with some text and a place for a video
A section for 'About Corvalen Remote Learning' with the text Corvalen Remote Learning has been providing distance education for over 40 years and have been the leader in online education for over 25 years.
Benefit from the resources and experience of one of the worlds leading course content providers.
Our highly qualified academic staff, HUGE resource library of up to date courses and cutting edge white label LMS enable our affiliates to stay well ahead of their competitors
A section for 'Free information pack' like the one on https://www.studyharbor.online/
Target Market(s)
Education providers looking to licence our courses to sell
Number of Pages Required
1 page
Look and feel

```html
<!DOCTYPE html>
<html lang="en">
<head>
<meta charset="utf-8">
<title>Corvalen Remote Learning – Affiliate Program</title>
<link href="https://fonts.googleapis.com/css2?family=Raleway:wght@300;400;500;600;700&display=swap" rel="stylesheet">
<style>
:root{
  --coral:#f05d5b;
  --page:#fdfaf5;
  --screen:#f6f5f4;
  --ink:#1f1f1f;
  --muted:#8a8a8a;
  --white:#ffffff;
  --photo-light:#e9e6e3;
  --photo-mid:#cfc6bd;
}
*{margin:0;padding:0;box-sizing:border-box}
html,body{width:1200px;height:2834px;overflow:hidden}
body{background:var(--page);font-family:'Raleway',sans-serif;color:var(--ink);position:relative}
.screen{position:absolute;top:71px;background:var(--screen);overflow:hidden}
.desktop{left:71px;width:779px;height:2698px}
.mobile{left:903px;width:222px;height:2700px}
.abs{position:absolute}
.band{position:absolute;left:0;right:0;background:var(--coral);color:var(--white)}
.center{text-align:center}
.photo{position:absolute;background:linear-gradient(135deg,var(--photo-light),var(--photo-mid))}
.play{position:absolute;left:50%;top:50%;border-radius:50%;background:var(--white);transform:translate(-50%,-50%);display:flex;align-items:center;justify-content:center}
.play svg{fill:var(--coral)}
.btn-outline{position:absolute;border:2px solid var(--coral);border-radius:20px;color:var(--coral);font-weight:500;text-align:center;background:transparent;box-shadow:0 2px 4px rgba(240,93,91,.25)}
.field{position:absolute;background:var(--white);color:#c3c3c3;font-weight:500;padding-left:14px;text-transform:uppercase}
.submit{position:absolute;background:var(--white);color:var(--coral);font-weight:500;text-align:center}
.hl{color:var(--coral)}
/* desktop */
.d-logo{left:70px;top:17px;font-size:10px;font-weight:600;letter-spacing:.3px;line-height:1.3;display:flex;align-items:center;gap:6px}
.d-logo i{display:block;width:10px;height:10px;background:var(--ink)}
.d-nav{left:316px;top:25px;display:flex;gap:15px;font-size:10px;font-weight:600}
.d-nav a{color:var(--ink);text-decoration:none}
.d-nav a.active{color:var(--coral)}
.d-hero-bg{left:0;top:0;width:779px;height:446px;background:radial-gradient(circle at 150px 260px,#fbe9e7 0,#f6f5f4 300px)}
.d-hero-title{left:70px;top:140px;font-size:27px;font-weight:300;line-height:31px;width:400px}
.d-hero-copy{left:70px;top:254px;width:305px;font-size:7.5px;font-weight:600;color:var(--muted);line-height:11px}
.d-copy{font-size:7.5px;font-weight:600;line-height:12px}
.d-feature{position:absolute;top:1677px;width:195px;text-align:center}
.d-feature svg{stroke:var(--coral);fill:none;stroke-width:2.2}
.d-feature h3{font-size:13px;font-weight:400;margin:14px 0 18px}
.d-feature p{font-size:7.5px;font-weight:600;line-height:15.5px}
.d-list{list-style:none}
.d-list li{position:relative;padding-left:9px}
.d-list li::before{content:"";position:absolute;left:0;top:4px;width:4px;height:4px;border-radius:50%;background:var(--coral)}
/* mobile */
.m-copy{font-size:6px;font-weight:500;line-height:8.5px}
.m-feature{position:absolute;left:8px;width:206px;text-align:center}
.m-feature svg{stroke:var(--coral);fill:none;stroke-width:2.4}
.m-feature h3{font-size:12px;font-weight:600;margin:12px 0 14px}
.m-feature p{font-size:4.6px;font-weight:500;line-height:12.5px;color:#444}
.burger{right:10px;top:14px;width:16px}
.burger span{display:block;height:2px;background:#bbb;margin-bottom:3px}
</style>
</head>
<body>

<!-- DESKTOP -->
<div class="screen desktop">
  <div class="abs d-hero-bg"></div>
  <div class="abs d-logo"><i></i>Corvalen Remote Learning</div>
  <nav class="abs d-nav">
    <a class="active">Home</a><a>About us</a><a>Our Courses</a><a>LMS Platform</a><a>Affiliate Program</a><a>Contact Us</a>
  </nav>
  <h1 class="abs d-hero-title">Over 450 courses written by highly qualified academics with <span class="hl">real world experience.</span></h1>
  <p class="abs d-hero-copy">Lorem ipsum dolor sit amet, consectetur adipiscing elit. Tincidunt sit dui dui massa molestie adipiscing. Magna a, bibendum pulvinar amet eu sed sit aenean. Nunc, mauris quis nullam est elit sem purus tempus. Risus enim est diam duis. Urna nunc.</p>
  <div class="btn-outline" style="left:70px;top:318px;width:91px;height:27px;font-size:9px;line-height:23px">JOIN NOW</div>
  <div class="photo" role="img" aria-label="Smiling man in a white shirt pointing to the headline" style="left:460px;top:80px;width:270px;height:366px;background:radial-gradient(ellipse at 50% 55%,#eae7e3 0,#f6f5f4 70%)"></div>

  <div class="band center" style="top:446px;height:95px;padding-top:26px;font-size:19px;font-weight:300;line-height:23px">Join our thriving group of Affiliates<br>start your own online college!</div>

  <div class="photo" role="img" aria-label="Video still: two women planning at a whiteboard in a bright office" style="left:70px;top:571px;width:638px;height:262px">
    <div class="play" style="width:50px;height:50px"><svg width="18" height="20" viewBox="0 0 18 20"><path d="M2 0 18 10 2 20Z"/></svg></div>
  </div>
  <div class="abs d-copy" style="left:72px;top:864px;width:420px">
    <p style="margin-bottom:9px">No previous education experience required - tutors are available.</p>
    <ul class="d-list" style="margin-bottom:9px">
      <li>Are you looking for a new business venture?</li>
      <li>Do you want to be your own boss?</li>
      <li>Do you want to earn a great income, and still have a life?</li>
    </ul>
    <p style="margin-bottom:8px;line-height:10px">You might already be working in education, or perhaps you're part of an association that is looking to expand it's offerings to it's members, or, just a motivated business person!</p>
    <p>Don't reinvent the wheel - our business model works - and it's an affordable buy in.</p>
  </div>
  <div class="btn-outline" style="left:618px;top:949px;width:91px;height:27px;font-size:9px;line-height:23px">JOIN NOW</div>

  <div class="band center" style="top:1006px;height:435px">
    <h2 style="font-size:19px;font-weight:300;margin-top:30px">see how our LMS works</h2>
    <p class="d-copy" style="width:640px;margin:14px auto 0;line-height:15.5px">Lorem ipsum dolor sit amet, consectetur adipiscing elit. Quis lacus at porttitor libero vitae aenean tortor ut. Turpis quisque pharetra faucibus orci ac risus sodales orci. Vitae duis turpis senectus euismod rutrum cras dolor. Semper massa, vitae justo, sapien arcu. Mauris, etiam nisl, pellentesque porttitor morbi lobortis et morbi.</p>
    <div class="photo" role="img" aria-label="Video still: hand with pen writing in a spiral notebook beside a laptop" style="left:70px;top:110px;width:638px;height:262px;background:linear-gradient(135deg,#d8c4ad,#efe7de 60%,#c9b39a)">
      <div class="play" style="width:50px;height:50px"><svg width="18" height="20" viewBox="0 0 18 20"><path d="M2 0 18 10 2 20Z"/></svg></div>
    </div>
  </div>

  <div class="abs" style="left:0;top:1441px;width:779px;height:481px;background:radial-gradient(circle at 120px 230px,#fbebe9 0,#f6f5f4 260px)"></div>
  <h2 class="abs center hl" style="left:0;width:779px;top:1471px;font-size:19px;font-weight:300">About us</h2>
  <p class="abs d-copy center" style="left:70px;width:640px;top:1515px;line-height:15.5px">Lorem ipsum dolor sit amet, consectetur adipiscing elit. Quis lacus at porttitor libero vitae aenean tortor ut. Turpis quisque pharetra faucibus orci ac risus sodales orci. Vitae duis turpis senectus euismod rutrum cras dolor. Semper massa, vitae justo, sapien arcu. Mauris, etiam nisl, pellentesque porttitor morbi lobortis et morbi. Augue a lacus commodo id nisi, ac a. Duis nec eu in sollicitudin in porta. Bibendum a purus, consequat aenean at suspendisse at dictumst sit. Pulvinar eget facilisis nunc dolor risus. Turpis sed eu arcu amet ipsum pellentesque. Vestibulum, tempor, at orci amet ut fermentum euismod nisl in. Nunc fringilla mauris sed urna, sem pharetra aliquam. Vulputate non risus sed egestas turpis integer.<br>Nibh eget ut ut semper gravida. Urna odio ligula consequat sed. Cursus pharetra vitae sem at amet purus sit.</p>

  <div class="d-feature" style="left:76px">
    <svg width="34" height="34" viewBox="0 0 34 34"><circle cx="17" cy="17" r="5"/><path d="M17 3l3 4 5-1 1 5 4 3-2 4 2 4-4 3-1 5-5-1-3 4-3-4-5 1-1-5-4-3 2-4-2-4 4-3 1-5 5 1z"/></svg>
    <h3>Delivering our courses</h3>
    <p>Lorem ipsum dolor sit amet, consectetur adipiscing elit. Quis lacus at porttitor libero vitae aenean tortor ut. Turpis quisque pharetra faucibus orci ac risus sodales orci. Vitae duis turpis senectus euismod rutrum cras dolor. Semper massa, vitae justo, sapien arcu.</p>
  </div>
  <div class="d-feature" style="left:293px">
    <svg width="34" height="34" viewBox="0 0 34 34"><rect x="6" y="2" width="22" height="30" rx="2"/><path d="M12 2v11l4-3 4 3V2"/></svg>
    <h3>Selling our ebooks</h3>
    <p>Lorem ipsum dolor sit amet, consectetur adipiscing elit. Quis lacus at porttitor libero vitae aenean tortor ut. Turpis quisque pharetra faucibus orci ac risus sodales orci. Vitae duis turpis senectus euismod rutrum cras dolor. Semper massa, vitae justo, sapien arcu. Mauris.</p>
  </div>
  <div class="d-feature" style="left:509px">
    <svg width="34" height="34" viewBox="0 0 34 34"><circle cx="17" cy="10" r="6"/><path d="M4 31v-3c0-5 5-8 13-8s13 3 13 8v3z"/></svg>
    <h3>Extra support available</h3>
    <p>Lorem ipsum dolor sit amet, consectetur adipiscing elit. Quis lacus at porttitor libero vitae aenean tortor ut. Turpis quisque pharetra faucibus orci ac risus sodales orci. Vitae duis turpis senectus euismod rutrum cras dolor. Semper massa, vitae justo, sapien arcu.</p>
  </div>

  <div class="band center" style="top:1922px;height:435px">
    <h2 style="font-size:19px;font-weight:300;margin-top:47px">Contact us</h2>
    <p style="font-size:7px;font-weight:600;margin-top:10px">Contact us now to discuss how we can work together to launch your own Distance Education Business...</p>
    <div class="field" style="left:179px;top:134px;width:205px;height:32px;font-size:8px;line-height:32px">Name</div>
    <div class="field" style="left:395px;top:134px;width:205px;height:32px;font-size:8px;line-height:32px">Phone</div>
    <div class="field" style="left:179px;top:183px;width:421px;height:32px;font-size:8px;line-height:32px">Email</div>
    <div class="field" style="left:179px;top:232px;width:421px;height:120px;font-size:8px;padding-top:10px">Detail</div>
    <div class="submit" style="left:492px;top:368px;width:108px;height:28px;font-size:12px;line-height:28px">Contact us</div>
  </div>

  <h2 class="abs center hl" style="left:0;width:779px;top:2394px;font-size:19px;font-weight:300">Becoming an Affiliate</h2>
  <div class="abs d-copy" style="left:62px;top:2442px;width:500px;line-height:15.5px">
    <p style="margin-bottom:16px">CRL works with affiliates who are like-minded and compatible.</p>
    <p style="margin-bottom:16px">To become an Affiliate, you must want to:</p>
    <div style="padding-left:9px">
      <p>Increase sales in your existing business (start-ups are encouraged to talk to us)</p>
      <p>Grow your business into a six-figure plus annual operation</p>
      <p>Work within simple contract terms</p>
      <p>Have autonomy from our brand</p>
      <p>Follow our model or go your own way</p>
      <p>Take advantage of support or training as much or as little as you need</p>
      <p>Get started for an extremely affordable establishment fee</p>
      <p>Boost your business by diversifying your product range</p>
      <p>Work with a trusted and established company</p>
    </div>
  </div>
  <div class="band center" style="top:2673px;height:25px;font-size:7px;font-weight:600;line-height:25px">Copyright © 2021 Corvalen Remote Learning</div>
</div>

<!-- MOBILE -->
<div class="screen mobile">
  <div class="abs burger"><span></span><span></span><span></span></div>
  <h1 class="abs" style="left:11px;top:71px;width:180px;font-size:10.5px;font-weight:600;line-height:12.5px">Over 450 courses written by highly qualified academics with <span class="hl">real world experience.</span></h1>
  <p class="abs m-copy" style="left:11px;top:118px;width:202px;color:var(--muted);font-size:5px;line-height:8.5px">Lorem ipsum dolor sit amet, consectetur adipiscing elit. Tincidunt sit dui dui massa molestie adipiscing. Magna a, bibendum pulvinar amet eu sed sit aenean. Nunc, mauris quis nullam est elit sem purus tempus. Risus enim est diam duis. Urna nunc.</p>
  <div class="btn-outline" style="left:11px;top:181px;width:99px;height:29px;font-size:9px;line-height:25px">JOIN NOW</div>
  <div class="photo" role="img" aria-label="Smiling man in a white shirt pointing upward" style="left:20px;top:225px;width:190px;height:257px;background:radial-gradient(ellipse at 50% 55%,#eae7e3 0,#f6f5f4 72%)"></div>
  <div class="band center" style="top:482px;height:104px;padding-top:40px;font-size:9.5px;font-weight:600;line-height:12px">Join our thriving group of Affiliates<br>start your own online college!</div>
  <div class="photo" role="img" aria-label="Video still: two women planning at a whiteboard" style="left:0;top:603px;width:222px;height:95px">
    <div class="play" style="width:36px;height:36px"><svg width="13" height="15" viewBox="0 0 18 20"><path d="M2 0 18 10 2 20Z"/></svg></div>
  </div>
  <div class="abs m-copy" style="left:11px;top:715px;width:202px">
    <p style="margin-bottom:7px">No previous education experience required - tutors are available.</p>
    <ul class="d-list" style="margin-bottom:7px">
      <li>Are you looking for a new business venture?</li>
      <li>Do you want to be your own boss?</li>
      <li>Do you want to earn a great income, and still have a life?</li>
    </ul>
    <p style="margin-bottom:7px">You might already be working in education, or perhaps you're part of an association that is looking to expand it's offerings to it's members, or, just a motivated business person!</p>
    <p>Don't reinvent the wheel - our business model works - and it's an affordable buy in.</p>
  </div>
  <div class="btn-outline" style="left:11px;top:870px;width:99px;height:29px;font-size:9px;line-height:25px">JOIN NOW</div>

  <div class="band center" style="top:932px;height:284px">
    <h2 style="font-size:9.5px;font-weight:600;margin-top:33px">see how our LMS works</h2>
    <p style="font-size:5px;font-weight:500;line-height:12.5px;width:210px;margin:8px auto 0">Lorem ipsum dolor sit amet, consectetur adipiscing elit. Quis lacus at porttitor libero vitae aenean tortor ut. Turpis quisque pharetra faucibus orci ac risus sodales orci. Vitae duis turpis senectus euismod rutrum cras dolor. Semper massa, vitae justo, sapien arcu. Mauris, etiam nisl, pellentesque porttitor morbi lobortis et morbi.</p>
    <div class="photo" role="img" aria-label="Video still: hand writing in a spiral notebook beside a laptop" style="left:0;top:133px;width:222px;height:114px;background:linear-gradient(135deg,#d8c4ad,#efe7de 60%,#c9b39a)">
      <div class="play" style="width:38px;height:38px"><svg width="13" height="15" viewBox="0 0 18 20"><path d="M2 0 18 10 2 20Z"/></svg></div>
    </div>
  </div>

  <h2 class="abs center hl" style="left:0;width:222px;top:1249px;font-size:9.5px;font-weight:600">About us</h2>
  <p class="abs center" style="left:9px;width:204px;top:1275px;font-size:4.8px;font-weight:500;line-height:12.2px;color:#444">Lorem ipsum dolor sit amet, consectetur adipiscing elit. Quis lacus at porttitor libero vitae aenean tortor ut. Turpis quisque pharetra faucibus orci ac risus sodales orci. Vitae duis turpis senectus euismod rutrum cras dolor. Semper massa, vitae justo, sapien arcu. Mauris, etiam nisl, pellentesque porttitor morbi lobortis et morbi. Augue a lacus commodo id nisi, ac a. Duis nec eu in sollicitudin in porta. Bibendum a purus, consequat aenean at suspendisse at dictumst sit. Pulvinar eget facilisis nunc dolor risus. Turpis sed eu arcu amet ipsum pellentesque. Vestibulum, tempor, at orci amet ut fermentum euismod nisl in. Nunc fringilla mauris sed urna, sem pharetra aliquam. Vulputate non risus sed egestas turpis integer.<br>Nibh eget ut ut semper gravida. Urna odio ligula consequat sed. Cursus pharetra vitae sem at amet purus sit.</p>

  <div class="m-feature" style="top:1487px">
    <svg width="38" height="38" viewBox="0 0 34 34"><circle cx="17" cy="17" r="5"/><path d="M17 3l3 4 5-1 1 5 4 3-2 4 2 4-4 3-1 5-5-1-3 4-3-4-5 1-1-5-4-3 2-4-2-4 4-3 1-5 5 1z"/></svg>
    <h3>Delivering our courses</h3>
    <p>Lorem ipsum dolor sit amet, consectetur adipiscing elit. Quis lacus at porttitor libero vitae aenean tortor ut. Turpis quisque pharetra faucibus orci ac risus sodales orci. Vitae duis turpis senectus euismod rutrum cras dolor. Semper massa, vitae justo, sapien arcu.</p>
  </div>
  <div class="m-feature" style="top:1670px">
    <svg width="40" height="46" viewBox="0 0 34 34"><rect x="6" y="2" width="22" height="30" rx="2"/><path d="M12 2v11l4-3 4 3V2"/></svg>
    <h3>Selling our ebooks</h3>
    <p>Lorem ipsum dolor sit amet, consectetur adipiscing elit. Quis lacus at porttitor libero vitae aenean tortor ut. Turpis quisque pharetra faucibus orci ac risus sodales orci. Vitae duis turpis senectus euismod rutrum cras dolor. Semper massa, vitae justo, sapien arcu. Mauris.</p>
  </div>
  <div class="m-feature" style="top:1876px">
    <svg width="38" height="38" viewBox="0 0 34 34"><circle cx="17" cy="10" r="6"/><path d="M4 31v-3c0-5 5-8 13-8s13 3 13 8v3z"/></svg>
    <h3>Extra support available</h3>
    <p>Lorem ipsum dolor sit amet, consectetur adipiscing elit. Quis lacus at porttitor libero vitae aenean tortor ut. Turpis quisque pharetra faucibus orci ac risus sodales orci. Vitae duis turpis senectus euismod rutrum cras dolor. Semper massa, vitae justo, sapien arcu.</p>
  </div>

  <div class="band center" style="top:2059px;height:347px">
    <h2 style="font-size:9.5px;font-weight:600;margin-top:31px">Contact us</h2>
    <p style="font-size:4.8px;font-weight:500;width:160px;margin:7px auto 0;line-height:6.5px">Contact us now to discuss how we can work together to launch your own Distance Education Business...</p>
    <div class="field" style="left:11px;top:103px;width:99px;height:27px;font-size:6px;line-height:27px">Name</div>
    <div class="field" style="left:114px;top:103px;width:98px;height:27px;font-size:6px;line-height:27px">Phone</div>
    <div class="field" style="left:11px;top:143px;width:201px;height:27px;font-size:6px;line-height:27px">Email</div>
    <div class="field" style="left:11px;top:186px;width:201px;height:100px;font-size:6px;padding-top:10px">Detail</div>
    <div class="submit" style="left:124px;top:306px;width:88px;height:23px;font-size:6.5px;font-weight:600;line-height:23px">Contact us</div>
  </div>

  <h2 class="abs center hl" style="left:0;width:222px;top:2439px;font-size:9.5px;font-weight:600">Becoming an Affiliate</h2>
  <div class="abs" style="left:11px;top:2466px;width:204px;font-size:5px;font-weight:500;line-height:12px;color:#444">
    <p style="margin-bottom:12px">CRL works with affiliates who are like-minded and compatible.</p>
    <p style="margin-bottom:12px">To become an Affiliate, you must want to:</p>
    <p>&nbsp;&nbsp;&nbsp;Increase sales in your existing business (start-ups are encouraged to talk to us)</p>
    <p>&nbsp;&nbsp;&nbsp;Grow your business into a six-figure plus annual operation</p>
    <p>&nbsp;&nbsp;&nbsp;Work within simple contract terms</p>
    <p>&nbsp;&nbsp;&nbsp;Have autonomy from our brand</p>
    <p>&nbsp;&nbsp;&nbsp;Follow our model or go your own way</p>
    <p>&nbsp;&nbsp;&nbsp;Take advantage of support or training as much or as little as you need</p>
    <p>&nbsp;&nbsp;&nbsp;Get started for an extremely affordable establishment fee</p>
    <p>&nbsp;&nbsp;&nbsp;Boost your business by diversifying your product range</p>
    <p>&nbsp;&nbsp;&nbsp;Work with a trusted and established company</p>
  </div>
  <div class="band center" style="top:2673px;height:27px;font-size:5px;font-weight:500;line-height:27px">Copyright © 2021 Corvalen Remote Learning</div>
</div>

</body>
</html>
```